Business Card Design Project

Im an electrician and my company name is Kestrel Electrical
My main work is installing Lighting and Power Points, Home Theater Systems, TVS, Phones and Data
Im looking a business card, something nice, clean, modern and not to cluttered
Im open to sugestions
I dont mind if the "Services" is on the back on the business card
colours black, grey, white or the blue colour of my logo are prefered but not compulsory
any questions just message me
and please make it so if i need to edit the writing can do it easy. maybe by making it a seperate layer ?
My Details are.
Name - Peter Halloran
Job Title - Licenced Electrician
Mobile - 027 583 2174
Email - peter@kestrelelectrical.co.nz
Web - www.kestrelelectrical.co.nz
Services
Residential / Commercial
Lighting & Power
Heating & Ventilation
Automation
Phone & Data
Home Cinema
Sound Systems
TV, Antenna & Satellite
Digital Upgrades

```html
<!DOCTYPE html>
<html lang="en">
<head>
<meta charset="utf-8">
<title>Kestrel Electrical – Business Card Presentation</title>
<link href="https://fonts.googleapis.com/css2?family=Source+Sans+3:wght@400;600;700&display=swap" rel="stylesheet">
<style>
  :root {
    --stage: #000000;
    --label: #7d7d7d;
    --card-white: #ffffff;
    --brand-teal: #0cadbd;
    --ink-grey: #565f63;
    --text-white: #ffffff;
  }
  * { margin: 0; padding: 0; box-sizing: border-box; }
  html, body { width: 1200px; height: 1200px; overflow: hidden; background: var(--stage); }
  body { position: relative; font-family: "Source Sans 3", "Myriad Pro", sans-serif; }

  .label { position: absolute; left: 337px; color: var(--label); font-weight: 400; line-height: 1; }
  .label--kicker { top: 66px; font-size: 23px; }
  .label--title { top: 95px; font-size: 44px; }
  .label--front { top: 205px; font-size: 23px; }
  .label--back { top: 954px; font-size: 23px; }

  .card { position: absolute; left: 333px; width: 532px; height: 325px; }
  .card--front { top: 240px; background: var(--card-white); }
  .card--back { top: 616px; background: var(--brand-teal); }

  .brand { position: absolute; left: 32px; top: 30px; display: flex; align-items: center; gap: 12px; }
  .brand__square { width: 26px; height: 26px; background: var(--brand-teal); }
  .brand__name { font-size: 32px; font-weight: 700; color: var(--brand-teal); line-height: 1; }

  .contact { position: absolute; left: 167px; top: 150px; color: var(--ink-grey); }
  .contact__name { font-size: 41px; font-weight: 600; line-height: 1; }
  .contact__role { font-size: 20px; margin-top: 4px; line-height: 1.1; }
  .contact__mobile { font-size: 27px; color: var(--brand-teal); margin-top: 12px; line-height: 1.1; }
  .contact__line { font-size: 17px; line-height: 22px; }
  .contact__line:first-of-type { margin-top: 8px; }

  .back-brand { position: absolute; left: 26px; top: 140px; display: flex; align-items: center; gap: 12px; }
  .back-brand__square { width: 30px; height: 30px; background: var(--text-white); }
  .back-brand__name { font-size: 30px; font-weight: 700; color: var(--text-white); line-height: 1; }

  .services { position: absolute; left: 276px; top: 30px; color: var(--text-white); list-style: none; }
  .services__title { font-size: 23px; font-weight: 600; line-height: 28px; }
  .services__item { font-size: 20px; line-height: 27px; }

  .specs { position: absolute; left: 337px; top: 1040px; color: var(--label); font-size: 19px; }
  .specs__heading { line-height: 24px; margin-bottom: 9px; }
  .specs__row { display: flex; line-height: 25px; }
  .specs__key { width: 83px; }
  .specs__sep { width: 18px; }
</style>
</head>
<body>
  <p class="label label--kicker">Business Card Design</p>
  <p class="label label--title">Creative 2</p>

  <p class="label label--front">Front</p>
  <section class="card card--front">
    <div class="brand">
      <span class="brand__square"></span>
      <span class="brand__name">Kestrel Electrical</span>
    </div>
    <div class="contact">
      <p class="contact__name">Peter Halloran</p>
      <p class="contact__role">Licenced Electrician</p>
      <p class="contact__mobile">Mobile : 027 583 2174</p>
      <p class="contact__line">Email : peter@kestrelelectrical.co.nz</p>
      <p class="contact__line">www.kestrelelectrical.co.nz</p>
    </div>
  </section>

  <section class="card card--back">
    <div class="back-brand">
      <span class="back-brand__square"></span>
      <span class="back-brand__name">Kestrel</span>
    </div>
    <ul class="services">
      <li class="services__title">Services</li>
      <li class="services__item">- Residential / Commercial</li>
      <li class="services__item">- Lighting &amp; Power</li>
      <li class="services__item">- Heating &amp; Ventilation</li>
      <li class="services__item">- Automation</li>
      <li class="services__item">- Phone &amp; Data</li>
      <li class="services__item">- Home Cinema</li>
      <li class="services__item">- Sound Systems</li>
      <li class="services__item">- TV, Antenna &amp; Satellite</li>
      <li class="services__item">- Digital Upgrades</li>
    </ul>
  </section>
  <p class="label label--back">Back</p>

  <div class="specs">
    <p class="specs__heading">Printing Specs</p>
    <p class="specs__row"><span class="specs__key">Trim size</span><span class="specs__sep">:</span><span>W: 90 cms x H: 5.5cms</span></p>
    <p class="specs__row"><span class="specs__key">Printing</span><span class="specs__sep">:</span><span>2 colour Spot ink</span></p>
    <p class="specs__row"><span class="specs__key">Stock</span><span class="specs__sep">:</span><span>200 gsm Meridian Wove Diamond White</span></p>
  </div>
</body>
</html>
```